Creative IT Startup company web site

We are small IT startup based in Japan
We provide IT consulting services and in-house software development.
Currently we are lunching new campaign called "Sparks in motion" also with this campaign we want to build new web site. Please check out our new web site for more info about project: http://v2.vantorabyte.com
As yo see there are only text - we need to make this clear, modern and beautiful. We are looking for creative designer to bring this web site to life.

Also some more information can be taken from our old web site: www.vantorabyte.com

Target Market(s)

IT entrepreneurs, Small companies, Anyone who has an idea and want to bring it to life.

Industry/Entity Type

It Company

Colors
86cfc6
85cae6

Requirements
Must have
• Single Page layout as a main page (instead of Hone and About)
this page should be called Sparks in Motion.

```html
<!DOCTYPE html>
<html lang="en">
<head>
<meta charset="utf-8">
<title>Vantorabyte – Sparks in Motion</title>
<link href="https://fonts.googleapis.com/css2?family=Noto+Serif:ital,wght@0,400;0,700;1,400;1,700&display=swap" rel="stylesheet">
<style>
:root{
  --green:#78c22a;
  --green-dark:#66a91f;
  --ink:#3f3f3f;
  --text:#555;
  --muted:#888;
  --line:#d8d8d8;
  --nav:#ececec;
  --dark:#1f1f1f;
  --white:#fff;
}
*{margin:0;padding:0;box-sizing:border-box}
html,body{width:1200px;height:2711px;overflow:hidden;background:var(--white)}
body{font-family:"Noto Serif",Georgia,serif;color:var(--text)}
.page{position:relative;width:1200px;height:2711px;overflow:hidden}
.abs{position:absolute}
.ital{font-style:italic;font-weight:700}

/* header */
.brand{left:69px;top:22px;display:flex;align-items:center;gap:14px}
.brand-dot{width:56px;height:56px;border-radius:50%;background:var(--green)}
.brand-name{font-size:38px;color:var(--green);font-weight:700;letter-spacing:.5px}
.contact{left:618px;top:28px;display:flex;gap:16px;align-items:center}
.contact p{font-size:16px;font-style:italic;color:#666;line-height:24px}
.social{left:900px;top:36px;display:flex;gap:8px}
.social span{width:31px;height:31px;border-radius:50%;background:#b8b8b8;display:block}
.social span:first-child{background:#3e5a98}

/* nav */
.nav{left:0;top:101px;width:1200px;height:49px;background:linear-gradient(#f4f4f4,#e2e2e2);border-bottom:1px solid #cfcfcf}
.nav a{position:absolute;top:0;height:49px;line-height:49px;font-size:17px;color:#444;text-decoration:none}
.nav a.active{background:var(--green);color:#fff;padding:0 22px}
.nav .sep{position:absolute;top:12px;width:1px;height:25px;background:#c9c9c9}
.search{left:1008px;top:0;width:60px;height:49px;background:#333}
.lang{left:1070px;top:0;width:60px;height:49px;background:var(--green);display:flex;align-items:center;justify-content:center}
.lang span{width:44px;height:28px;background:linear-gradient(#2d3f8a,#24357a);display:block}

/* hero */
.hero{left:0;top:150px;width:1200px;height:515px;background:linear-gradient(90deg,#e4e4e4,#f3f3f3 60%,#fafafa)}
.hero-art{left:600px;top:172px;width:600px;height:493px;background:radial-gradient(ellipse at 55% 45%,#f9f9f9 0%,#e2e2e2 55%,rgba(228,228,228,0) 78%)}
.hero-title{left:69px;top:250px;width:520px;font-size:50px;color:#555;line-height:66px;white-space:nowrap;z-index:2}
.hero-title em{color:var(--green);font-style:italic}
.hero-text{left:69px;top:420px;width:510px;font-size:15.5px;line-height:26px;color:#333;z-index:2}
.dots{left:490px;top:652px;display:flex;gap:17px}
.dots span{width:27px;height:27px;border-radius:50%;background:#e8e8e8;border:2px solid #fff;box-shadow:0 0 0 1px #d2d2d2;font-size:10px;color:#999;text-align:center;line-height:23px;font-style:italic}
.dots span.on{background:var(--green);color:#fff}

/* welcome */
.h2{font-size:33px;font-style:italic;font-weight:700;color:#555;text-align:center;width:1200px;left:0}
.h2 em{color:var(--green)}
.welcome-text{left:108px;top:778px;width:984px;text-align:center;font-size:14.5px;line-height:25px}

/* services */
.band{left:0;top:967px;width:1200px;height:226px;background:var(--green)}
.service{top:912px;width:372px;text-align:center;color:#fff}
.service svg{display:block;margin:0 auto}
.service h3{font-size:22px;font-style:italic;font-weight:700;margin-top:24px}
.service p{font-size:15px;line-height:26px;margin:12px auto 0;width:340px}
.more{display:inline-block;margin-top:16px;width:108px;height:35px;background:#fff;color:var(--green);font-size:13px;font-style:italic;font-weight:700;line-height:35px}

/* build */
.build-bg{left:0;top:1193px;width:1200px;height:388px;background:linear-gradient(90deg,#f6f6f6,#ededed 50%,#f3f3f3)}
.build-title{left:69px;top:1232px;font-size:34px;color:var(--green)}
.rule{left:69px;top:1292px;width:262px;height:3px;background:#ccc}
.build-sub{left:69px;top:1320px;font-size:15px;color:#222}
.build-text{left:69px;top:1366px;width:660px;font-size:14.5px;line-height:25.5px}

/* team */
.team-sub{left:0;width:1200px;top:1668px;text-align:center;font-size:15.5px;font-style:italic;color:#444}

/* tweet */
.tweet-bg{left:0;top:2015px;width:1200px;height:193px;background:linear-gradient(90deg,#cfcfcf,#e8e8e8 50%,#d2d2d2)}
.tweet{left:69px;top:2060px;width:1061px;height:105px;background:#fff;border-left:5px solid var(--green);border-right:5px solid var(--green)}
.tweet-icon{left:18px;top:36px;width:34px;height:34px;border-radius:50%;background:var(--green)}
.tweet p{position:absolute;left:82px;top:28px;width:780px;font-size:16px;line-height:24px;color:#444}
.tweet p em{color:var(--green);font-style:normal}
.tweet time{position:absolute;right:22px;top:40px;font-size:17px;font-style:italic;color:var(--green)}

/* footer */
.foot-bg{left:0;top:2208px;width:1200px;height:445px;background:linear-gradient(160deg,#3a3a3a,#1d1d1d 60%,#151515)}
.tab{top:2208px;height:58px;line-height:58px;text-align:center;font-size:21px;font-style:italic;font-weight:700;color:#fff;background:#585858}
.tab.active{background:#262626;color:var(--green)}
.foot-head{left:69px;top:2334px;font-size:18px;color:var(--green)}
.row{font-size:15px;line-height:22px;color:#fff;white-space:nowrap}
.row b{color:var(--green);font-style:italic}
.lbl{text-align:right}
.map{left:815px;top:2294px;width:310px;height:310px;border-radius:50%;border:6px solid #555;background:radial-gradient(circle at 45% 45%,#eceae3,#d9d6cc 70%,#c9c5ba)}

/* bottom */
.bottom{left:0;top:2653px;width:1200px;height:58px;background:#111;font-size:13px;color:#fff;line-height:58px}
.bottom .links{position:absolute;left:69px}
.bottom .legal{position:absolute;right:70px}
.bottom .g{color:var(--green)}
</style>
</head>
<body>
<div class="page">

  <header>
    <div class="abs brand"><span class="brand-dot"></span><span class="brand-name">Vantorabyte</span></div>
    <div class="abs contact">
      <svg width="38" height="30" viewBox="0 0 38 30" aria-hidden="true"><rect x="1" y="8" width="30" height="21" fill="#78c22a"/><path d="M1 8 L16 19 L31 8" stroke="#fff" stroke-width="2" fill="none"/><path d="M28 1 c3 0 8 5 8 8 l-3 2 l-4-4 z" fill="#333"/></svg>
      <div><p>Call: +81 6 5550 0142</p><p>info@vantorabyte.com</p></div>
    </div>
    <div class="abs social" aria-label="Social links"><span></span><span></span><span></span><span></span><span></span><span></span></div>
  </header>

  <nav class="abs nav">
    <a class="active" style="left:69px">Home</a>
    <span class="sep" style="left:172px"></span>
    <a style="left:190px">Sparks in Motion</a>
    <span class="sep" style="left:350px"></span>
    <a style="left:369px">IT Consulting</a>
    <span class="sep" style="left:510px"></span>
    <a style="left:529px">Software Development</a>
    <span class="sep" style="left:755px"></span>
    <a style="left:773px">Carriers</a>
    <span class="sep" style="left:872px"></span>
    <a style="left:891px">Contact Us</a>
    <div class="abs search"><svg width="60" height="49" viewBox="0 0 60 49" aria-label="Search"><circle cx="27" cy="22" r="9" stroke="#fff" stroke-width="3" fill="none"/><path d="M33 28 L40 35" stroke="#fff" stroke-width="4"/></svg></div>
    <div class="abs lang"><span role="img" aria-label="Language: English flag"></span></div>
  </nav>

  <section>
    <div class="abs hero"></div>
    <div class="abs hero-art" role="img" aria-label="Light bulbs with coloured cables rising from a pot of pebbles"></div>
    <h1 class="abs hero-title ital">We bring your<br><em>SPARKS</em> in <em>MOTION</em></h1>
    <p class="abs hero-text">In May of 1899 Elias Marren wrote a letter to the Halden Institution with an idea in mind. On December 17, 1903 Elias, and his brother Tobias, invented and built the world's first airplane — and conducted the world's first successfully controlled, powered and heavier-than-air flight.</p>
    <div class="abs dots"><span>01</span><span>02</span><span class="on">03</span><span>04</span><span>05</span></div>
  </section>

  <section>
    <h2 class="abs h2" style="top:716px">Welcome to <em>Vantorabyte</em></h2>
    <p class="abs welcome-text">Lorem ipsum dolor sit amet, consectetur adipiscing elit. In ut ligula vitae dolor faucibus commodo accumsan nec lectus. Fusce ac magna vel urna semper dapibus. Sed non malesuada massa, eget tincidunt lectus. Ut eget ullamcorper turpis. Aliquam sit amet diam egestas, interdum orci at, sodales risus. Integer suscipit in magna eu sagittis. Morbi nec neque orci.</p>
  </section>

  <section>
    <div class="abs band"></div>
    <div class="abs service" style="left:42px">
      <svg width="116" height="96" viewBox="0 0 116 96" aria-hidden="true"><path d="M58 4 C86 2 112 22 110 52 C108 80 86 95 58 95 C28 95 6 80 6 52 C6 22 30 6 58 4Z" fill="#fff"/><circle cx="58" cy="50" r="30" fill="#78c22a"/><path d="M48 40 L38 50 L48 60 M68 40 L78 50 L68 60 M62 36 L54 64" stroke="#fff" stroke-width="3" fill="none"/></svg>
      <h3>Software Development</h3>
      <p>After many years in Software Project Delivery, Vantorabyte can help you at every stage of your project.</p>
      <span class="more">Read more</span>
    </div>
    <div class="abs service" style="left:414px">
      <svg width="116" height="96" viewBox="0 0 116 96" aria-hidden="true"><path d="M58 4 C86 2 112 22 110 52 C108 80 86 95 58 95 C28 95 6 80 6 52 C6 22 30 6 58 4Z" fill="#fff"/><circle cx="58" cy="50" r="30" fill="#78c22a"/><rect x="42" y="36" width="32" height="22" stroke="#fff" stroke-width="3" fill="none"/><path d="M52 64 H64 M58 58 V64" stroke="#fff" stroke-width="3"/></svg>
      <h3>Application Management</h3>
      <p>90% of the cost involved in managing software systems lies in maintenance phase – which is often neglected</p>
      <span class="more">Read more</span>
    </div>
    <div class="abs service" style="left:786px">
      <svg width="116" height="96" viewBox="0 0 116 96" aria-hidden="true"><path d="M58 4 C86 2 112 22 110 52 C108 80 86 95 58 95 C28 95 6 80 6 52 C6 22 30 6 58 4Z" fill="#fff"/><circle cx="58" cy="50" r="30" fill="#78c22a"/><circle cx="58" cy="46" r="11" fill="#fff"/><rect x="53" y="57" width="10" height="8" fill="#fff"/></svg>
      <h3>Improvement Management</h3>
      <p>We live today in a very high-paced society – organization who wish to excels will need to constantly evolve and innovate.</p>
      <span class="more">Read more</span>
    </div>
  </section>

  <section>
    <div class="abs build-bg" role="img" aria-label="Softly blurred crowd of people in the background"></div>
    <h2 class="abs build-title ital">Build your IDEA</h2>
    <div class="abs rule"></div>
    <p class="abs build-sub ital">We help to give you the means, the resources, and the people.</p>
    <p class="abs build-text">Lorem ipsum dolor sit amet, consectetur adipiscing elit. Donec ut nisl sed eros venenatis fermentum at sit amet felis. Curabitur et magna dui. Integer ipsum neque, lobortis nec luctus eget, facilisis non nisi. Vivamus ultricies erat vel lorem sodales suscipit. Nam eleifend diam sit amet mi mattis graida. Phasellus arcu dolor, varius ac iaculis ut, ullamcorper vel ipsum. Morbi velit nisi, vulputate id tnt eu, ullamcorper quis arcu. In hac habitasse platea dictumst. Nam era vt ligula, congue id enim ac, malesuada dapibus mi.</p>
    <svg class="abs" style="left:773px;top:1222px" width="312" height="344" viewBox="0 0 312 344" aria-hidden="true">
      <path d="M120 14 C190 -6 300 20 306 120 C312 230 280 330 170 340 C60 348 6 270 4 170 C2 80 40 30 120 14Z" fill="#78c22a"/>
      <ellipse cx="160" cy="180" rx="118" ry="132" fill="#f2f2f2"/>
    </svg>
    <div class="abs" style="left:815px;top:1262px;width:236px;height:264px;border-radius:50%;background:radial-gradient(circle,#f7f7f7,#e6e6e6)" role="img" aria-label="Colourful wooden construction sticks forming a lattice"></div>
  </section>

  <section>
    <h2 class="abs h2" style="top:1612px;color:var(--green)">Meet Your TEAM</h2>
    <p class="abs team-sub">We have the developers, project managers, designers and professionals for your team .</p>
    <svg class="abs" style="left:66px;top:1717px" width="1070" height="272" viewBox="0 0 1070 272" aria-hidden="true">
      <defs><path id="blob" d="M108 6 C170 0 222 50 222 130 C222 220 180 268 112 270 C44 272 2 220 2 130 C2 50 50 12 108 6Z"/></defs>
      <use href="#blob" x="0" fill="#78c22a"/>
      <use href="#blob" x="286" fill="#78c22a"/>
      <use href="#blob" x="566" fill="#78c22a"/>
      <use href="#blob" x="840" fill="#78c22a"/>
    </svg>
    <div class="abs" style="left:100px;top:1745px;width:176px;height:226px;border-radius:50%;background:radial-gradient(circle at 50% 40%,#d8d8d8,#8a8a8a)" role="img" aria-label="Team member portrait"></div>
    <div class="abs" style="left:386px;top:1745px;width:176px;height:226px;border-radius:50%;background:radial-gradient(circle at 50% 40%,#cfcfcf,#6f6f6f)" role="img" aria-label="Team member portrait"></div>
    <div class="abs" style="left:666px;top:1745px;width:176px;height:226px;border-radius:50%;background:radial-gradient(circle at 50% 40%,#d2d2d2,#7a7a7a)" role="img" aria-label="Team member portrait"></div>
    <div class="abs" style="left:940px;top:1745px;width:176px;height:226px;border-radius:50%;background:radial-gradient(circle at 50% 40%,#d5d5d5,#7d7d7d)" role="img" aria-label="Team member portrait"></div>
  </section>

  <section>
    <div class="abs tweet-bg" role="img" aria-label="Blurred office background"></div>
    <div class="abs tweet">
      <span class="abs tweet-icon"></span>
      <p>Lorem ipsum dolor sit amet, consectetur adipiscing elit. <em>Aenean hendrerit,</em> tellus in fermentum pellentesque . onsectetur adipiscing elit</p>
      <time>2 hour ago</time>
    </div>
  </section>

  <footer>
    <div class="abs foot-bg" role="img" aria-label="Dark blurred crowd background"></div>
    <div class="abs tab active" style="left:69px;width:354px">Japan Get in Touch!</div>
    <div class="abs tab" style="left:425px;width:352px">Spain Get in Touch!</div>
    <div class="abs tab" style="left:779px;width:351px">Ireland Get in Touch!</div>
    <h3 class="abs foot-head ital">E-Mail &amp; Location</h3>

    <div class="abs row lbl" style="left:40px;width:164px;top:2425px"><b>General enquires:</b></div>
    <div class="abs row" style="left:212px;top:2425px">info@vantorabyte.com</div>
    <div class="abs row lbl" style="left:40px;width:164px;top:2462px"><b>Support:</b></div>
    <div class="abs row" style="left:212px;top:2462px">support@vantorabyte.com</div>
    <div class="abs row lbl" style="left:40px;width:164px;top:2499px"><b>Sales:</b></div>
    <div class="abs row" style="left:212px;top:2499px">sales@vantorabyte.com</div>
    <div class="abs row lbl" style="left:40px;width:164px;top:2537px"><b>Sourcing:</b></div>
    <div class="abs row" style="left:212px;top:2537px">sourcing@vantorabyte.com</div>

    <div class="abs row lbl" style="left:420px;width:135px;top:2421px"><b>Osaka Office:</b></div>
    <div class="abs row" style="left:562px;top:2421px">2-8-15 Minamimachi, Kitaku,<br>Osakashi Osaka, Japan 530-0000</div>
    <div class="abs row lbl" style="left:420px;width:135px;top:2479px"><b>Tokyo Office:</b></div>
    <div class="abs row" style="left:562px;top:2479px">140-0000 Tokyo-to, Oota-ku,<br>Hikari 5-11-3</div>
    <div class="abs row lbl" style="left:420px;width:135px;top:2537px"><b>Phone:</b></div>
    <div class="abs row" style="left:562px;top:2537px">+81 6 5550 0142</div>

    <div class="abs map" role="img" aria-label="Street map of the Osaka office area"></div>

    <div class="abs bottom">
      <span class="links"><span class="g">Home</span> / Sparks in Motion / IT Consulting / Software Development / Carriers / Contact Us</span>
      <span class="legal">© 2014 <span class="g">Vantorabyte.</span> Privacy Policy / Term of Use / Site Map</span>
    </div>
  </footer>

</div>
</body>
</html>
```